Business Card Design

Electric home brewing equipment. Custom and catalog items. Most products are made by or for my company, so name is on most everything. Travel to conventions, to meet with home brewers. Trying to create a professional, but since primarily home brewers, fun image. New logo attached, with this new logo I'm redoing most materials. I'm trying to create a single brand under this logo.
Bolt icon on card, does not have to be directly over text as in logo file, but can be used similar to my example.

Website address is http://www.voltkettleworks.com (this is a must add).

New video intro to be added to video productions here: http://clipvault.example/k7Rm2xQwLp

Target Market(s)

Home brewers, predominantly male, ages 21 - 55, tend to be looking for the hot new thing.

Industry/Entity Type

Business

Contact Information for Business Card

Details as included on file. Layout I've attached is approximately what I'm looking for. Single and Double sided cards options welcome.

Card info should include:
2 cards: Derek Holm and Mona Holm
Both: Owners
Email: derek@voltkettleworks.com and mona@voltkettleworks.com
Both phone: 888-472-0635
Both address: Lakeview, Texas 77512
Website: voltkettleworks.com

Requirements
Must have
• Use both parts of the logo, not necessarily together as design should infer.

```html
<!DOCTYPE html>
<html lang="en">
<head>
<meta charset="utf-8">
<title>Volt Kettle Works – Business Card</title>
<link rel="stylesheet" href="https://fonts.googleapis.com/css2?family=Archivo+Black&family=Oswald:wght@400;500&family=Pinyon+Script&display=swap">
<style>
  :root {
    --backdrop: #e8e5e1;
    --card: #ffffff;
    --ink: #111111;
    --volt-yellow: #fbbd14;
  }
  * { box-sizing: border-box; margin: 0; padding: 0; }
  html, body {
    width: 1200px;
    height: 918px;
    overflow: hidden;
    background: var(--backdrop);
  }
  .business-card {
    position: absolute;
    left: 75px;
    top: 159px;
    width: 1050px;
    height: 600px;
    background: var(--card);
    box-shadow: 0 6px 24px rgba(0,0,0,0.12);
    overflow: hidden;
  }
  .brand-mark {
    position: absolute;
    left: 50px;
    top: 40px;
    width: 190px;
    height: 190px;
    border: 16px solid var(--ink);
    border-radius: 50%;
  }
  .brand-name {
    position: absolute;
    left: 268px;
    top: 98px;
    font-family: "Archivo Black", Arial, sans-serif;
    font-size: 66px;
    line-height: 1;
    color: var(--ink);
    letter-spacing: -1px;
    white-space: nowrap;
  }
  .role {
    position: absolute;
    left: 570px;
    top: 236px;
    width: 150px;
    text-align: center;
    font-family: "Oswald", Arial, sans-serif;
    font-size: 22px;
    color: var(--volt-yellow);
  }
  .person-name {
    position: absolute;
    left: 470px;
    top: 262px;
    width: 360px;
    text-align: center;
    font-family: "Pinyon Script", cursive;
    font-size: 66px;
    line-height: 1;
    color: var(--ink);
  }
  .contact-band {
    position: absolute;
    left: 50px;
    top: 345px;
    width: 860px;
    height: 110px;
  }
  .contact-band svg { position: absolute; left: 0; top: 0; }
  .contact-text {
    position: absolute;
    font-family: "Oswald", Arial, sans-serif;
    font-weight: 500;
    font-size: 26px;
    color: var(--ink);
    white-space: nowrap;
  }
  .email { left: 78px; top: 362px; }
  .phone { left: 640px; top: 410px; }
  .website { left: 72px; top: 478px; }
  .address { left: 690px; top: 510px; }
</style>
</head>
<body>
  <main class="business-card">
    <div class="brand-mark"></div>
    <div class="brand-name">Volt Kettle Works</div>

    <div class="role">Owner</div>
    <div class="person-name">Mona Holm</div>

    <div class="contact-band">
      <svg width="960" height="130" viewBox="0 0 960 130" aria-hidden="true">
        <polygon points="0,0 860,40 830,110 0,110" fill="var(--volt-yellow)" transform="translate(0,0) scale(1,1)"/>
      </svg>
    </div>
    <svg class="band-tab" width="1050" height="600" viewBox="0 0 1050 600" style="position:absolute;left:0;top:0" aria-hidden="true">
      <polygon points="50,345 890,345 855,455 50,455" fill="var(--volt-yellow)"/>
      <polygon points="895,400 985,400 960,470 870,470" fill="var(--ink)"/>
    </svg>

    <div class="contact-text email">mona@voltkettleworks.com</div>
    <div class="contact-text phone">888.472-0635</div>
    <div class="contact-text website">www.voltkettleworks.com</div>
    <div class="contact-text address">Lakeview, Texas 77512</div>
  </main>
</body>
</html>
```